Publisher needs a book cover design for ‘Lanterns Over the Marsh Gate’ book

We need a book cover (front, back, spine) for the 2nd edition of a book entitled ‘Lanterns Over the Marsh Gate’ and subtitled ‘the quiet geography of tidal winds, ferry routes and harbour lanterns’ (inverted commas not to be part of the title and subtitle). The author is Rupert Calloway. The publisher is Vellmark Press. The finished size of the paperback version will be the industry standard 9" x 6". There will be paperback, hardback, and e-book versions. The final number of pages is expected to be in the region 150-180 pages. Text for the back cover is not yet available, but at the bottom of the back cover should be publisher logo (rectangular) on the left and space for the ISBN bar code on the right. The circular logo should be on the spine. The design should be original and not include any stock images that have been created by someone else or may require obtaining a copyright licence to use. Symbols in common use and not copyrighted are probably ok. There are no required images, photographs or symbols except the publisher logo at the left bottom of the back cover and lower spine. Spine lettering should be UK/US style with the top of the writing nearest the front cover. The designer is free to be creative using appropriate diagrams, symbols or abstract designs. Rectangular and circular variants of the publisher logo are attached. Designers are assured that when evaluating designs absolutely no notice whatsoever is taken of a designer's Pixo Rally ranking or status; We are completely output driven, so what matters is the design, not the ranking or status of the designer. In a similar way, designs are not evaluated as 'good' or 'bad' - the winning design will be chosen after review by a design review panel and is not decided arbitrarily by a single person. All submitted designs should be capable of effective copyright assignment.

Target Market(s)

Practitioners, parents, teachers, pupils and academics concerned with child protection, safeguarding and the elimination of emotional abuse of children in the classroom

Font styles to use
Serif
Sans Serif

Requirements
Must have
• • Title, author, edition, subtitle, publisher logo
Nice to have
• • Originality, innovation
Should not have
• • Stock images or anything else requiring additional copyright discussions and negotiations.

```html
<!DOCTYPE html>
<html lang="en">
<head>
<meta charset="utf-8">
<title>Lanterns Over the Marsh Gate – 2nd Edition Cover</title>
<link rel="stylesheet" href="https://fonts.googleapis.com/css2?family=Cabin+Sketch:wght@700&family=Anton&family=Oswald:wght@300;400&family=Roboto+Condensed:wght@400&family=Architects+Daughter&display=swap">
<style>
  :root {
    --board-light: #3f5a48;
    --board-mid: #2f4738;
    --board-dark: #22352a;
    --board-panel: #263a2e;
    --band-red: #d3141b;
    --band-red-dark: #b80f15;
    --footer-brown: #6a2a1d;
    --chalk-white: #f4f4ef;
    --chalk-red: #e0141c;
    --edition-orange: #f08a1c;
    --ink-white: #ffffff;
  }
  * { margin: 0; padding: 0; box-sizing: border-box; }
  html, body { width: 1200px; height: 844px; overflow: hidden; background: #ffffff; }
  .cover { position: relative; width: 1200px; height: 844px; overflow: hidden; }
  .cover-ground { position: absolute; inset: 0; }

  .chalk-title {
    position: absolute;
    font-family: "Cabin Sketch", "Comic Sans MS", cursive;
    font-weight: 700;
    color: var(--chalk-white);
    text-transform: uppercase;
    text-align: center;
    white-space: nowrap;
  }
  .chalk-title span { display: block; }
  .chalk-title .accent { color: var(--chalk-red); }
  .edition {
    position: absolute;
    font-family: "Architects Daughter", cursive;
    color: var(--edition-orange);
    text-transform: uppercase;
    letter-spacing: 2px;
    white-space: nowrap;
  }
  .edition sup { font-size: 55%; }

  /* Back cover */
  .back-title { left: 113px; top: 52px; width: 320px; font-size: 32px; line-height: 40px; }
  .back-edition { left: 300px; top: 176px; font-size: 15px; line-height: 20px; }
  .back-copy {
    position: absolute; left: 120px; top: 218px; width: 408px;
    font-family: "Roboto Condensed", "Arial Narrow", sans-serif;
    font-size: 8px; line-height: 11.25px; letter-spacing: 0.2px;
    color: var(--ink-white); text-transform: uppercase;
  }
  .back-imprint { position: absolute; left: 45px; top: 712px; display: flex; align-items: center; gap: 10px; }
  .back-imprint .mark-dot { width: 60px; height: 60px; border-radius: 50%; background: var(--ink-white); }
  .back-imprint .imprint-name { font-family: "Oswald", sans-serif; font-weight: 400; font-size: 26px; letter-spacing: 1px; color: var(--ink-white); text-transform: uppercase; }
  .isbn-space { position: absolute; left: 395px; top: 712px; width: 145px; height: 73px; background: var(--ink-white); }

  /* Spine */
  .spine-title, .spine-author {
    position: absolute; left: 582px; transform: translateX(-50%);
    writing-mode: vertical-rl; white-space: nowrap; text-transform: uppercase;
  }
  .spine-title { top: 18px; font-family: "Cabin Sketch", cursive; font-weight: 700; font-size: 22px; line-height: 30px; letter-spacing: 0.5px; color: var(--chalk-white); }
  .spine-title .accent { color: var(--chalk-red); }
  .spine-edition { font-family: "Architects Daughter", cursive; font-size: 8px; color: var(--edition-orange); letter-spacing: 1px; }
  .spine-author { top: 490px; font-family: "Anton", "Impact", sans-serif; font-size: 26px; line-height: 32px; letter-spacing: 1.5px; color: var(--ink-white); }
  .spine-imprint { position: absolute; left: 556px; top: 760px; width: 52px; text-align: center; }
  .spine-imprint .mark-dot { display: block; width: 36px; height: 36px; border-radius: 50%; background: var(--ink-white); margin: 0 auto 5px; }
  .spine-imprint .imprint-name { font-family: "Oswald", sans-serif; font-weight: 400; font-size: 9px; letter-spacing: 0.5px; color: var(--ink-white); text-transform: uppercase; }

  /* Front cover */
  .front-title { left: 640px; top: 76px; width: 580px; font-size: 80px; line-height: 85px; letter-spacing: 1px; }
  .front-edition { left: 930px; top: 410px; font-size: 28px; line-height: 34px; }
  .subtitle { position: absolute; left: 660px; top: 470px; width: 530px; color: var(--ink-white); text-transform: uppercase; white-space: nowrap; }
  .subtitle-lead { font-family: "Oswald", sans-serif; font-weight: 400; font-size: 26px; line-height: 34px; letter-spacing: 2.4px; }
  .subtitle-main { font-family: "Anton", "Impact", sans-serif; font-size: 50px; line-height: 57px; letter-spacing: 1px; margin-top: 2px; }
  .front-rule { position: absolute; left: 690px; width: 510px; height: 2px; background: var(--ink-white); }
  .front-rule.is-second { left: 720px; }
  .front-author { position: absolute; left: 640px; top: 750px; width: 560px; font-family: "Anton", "Impact", sans-serif; font-size: 58px; line-height: 72px; letter-spacing: 2px; color: var(--ink-white); text-transform: uppercase; text-align: center; }
</style>
</head>
<body>
<main class="cover">
  <svg class="cover-ground" width="1200" height="844" viewBox="0 0 1200 844" aria-hidden="true">
    <defs>
      <radialGradient id="board" cx="0.6" cy="0.15" r="0.8">
        <stop offset="0" stop-color="var(--board-light)"/>
        <stop offset="0.6" stop-color="var(--board-mid)"/>
        <stop offset="1" stop-color="var(--board-dark)"/>
      </radialGradient>
      <linearGradient id="band" x1="0" y1="0" x2="0" y2="1">
        <stop offset="0" stop-color="var(--band-red)"/>
        <stop offset="1" stop-color="var(--band-red-dark)"/>
      </linearGradient>
    </defs>
    <rect width="1200" height="844" fill="url(#board)"/>
    <rect x="82" y="212" width="466" height="90" fill="var(--board-panel)" opacity="0.6"/>
    <path d="M0 270 C200 262 430 298 600 330 C790 366 1000 430 1200 452 L1200 735 L0 735 Z" fill="url(#band)"/>
    <rect y="735" width="1200" height="109" fill="var(--footer-brown)"/>
  </svg>

  <!-- Back cover -->
  <h2 class="chalk-title back-title"><span>Lanterns</span><span class="accent">Over</span><span>The Marsh Gate</span></h2>
  <div class="edition back-edition">2<sup>nd</sup> Edition</div>
  <div class="back-copy">
    <p>Along the estuary the evening tide carries small boats between quiet harbours, and every ferry lane is marked by lanterns that glow above the old marsh gate. This book follows those routes across the water, the winds that shape them from season to season, and the keepers who light the way when fog rolls in from the sea. It maps the sandbanks, the channels and the landing stages that still serve the villages along the shore.</p>
    <p>Each chapter pairs a tidal chart with field notes gathered on the crossings, showing how light, weather and water together guide travellers safely home through the long night. Readers will find route tables, wind roses and a glossary of harbour terms.</p>
    <p>Along the estuary the evening tide carries small boats between quiet harbours, and every ferry lane is marked by lanterns that glow above the old marsh gate. This book follows those routes across the water, the winds that shape them from season to season, and the keepers who light the way when fog rolls in from the sea. It maps the sandbanks, the channels and the landing stages that still serve the villages along the shore.</p>
    <p>Each chapter pairs a tidal chart with field notes gathered on the crossings, showing how light, weather and water together guide travellers safely home through the long night. Readers will find route tables, wind roses and a glossary of harbour terms.</p>
    <p>Along the estuary the evening tide carries small boats between quiet harbours, and every ferry lane is marked by lanterns that glow above the old marsh gate. This book follows those routes across the water, the winds that shape them from season to season, and the keepers who light the way when fog rolls in from the sea. It maps the sandbanks, the channels and the landing stages that still serve the villages along the shore.</p>
    <p>Each chapter pairs a tidal chart with field notes gathered on the crossings, showing how light, weather and water together guide travellers safely home through the long night. Readers will find route tables, wind roses and a glossary of harbour terms.</p>
    <p>Along the estuary the evening tide carries small boats between quiet harbours, and every ferry lane is marked by lanterns that glow above the old marsh gate. This book follows those routes across the water, the winds that shape them from season to season, and the keepers who light the way when fog rolls in from the sea. It maps the sandbanks, the channels and the landing stages that still serve the villages along the shore.</p>
    <p>Each chapter pairs a tidal chart with field notes gathered on the crossings, showing how light, weather and water together guide travellers safely home through the long night. Readers will find route tables, wind roses and a glossary of harbour terms.</p>
    <p>Along the estuary the evening tide carries small boats between quiet harbours, and every ferry lane is marked by lanterns that glow above the old marsh gate. This book follows those routes across the water, the winds that shape them from season to season, and the keepers who light the way when fog rolls in from the sea. It maps the sandbanks, the channels and the landing stages that still serve the villages along the shore.</p>
  </div>
  <div class="back-imprint"><span class="mark-dot"></span><span class="imprint-name">Vellmark Press</span></div>
  <div class="isbn-space" aria-label="Space for ISBN bar code"></div>

  <!-- Spine -->
  <div class="spine-title">Lanterns <span class="accent">Over</span> The Marsh Gate <span class="spine-edition">2nd Edition</span></div>
  <div class="spine-author">Rupert Calloway</div>
  <div class="spine-imprint"><span class="mark-dot"></span><span class="imprint-name">Vellmark</span></div>

  <!-- Front cover -->
  <h1 class="chalk-title front-title"><span>Lanterns</span><span class="accent">Over</span><span>The Marsh</span><span>Gate</span></h1>
  <div class="edition front-edition">2<sup>nd</sup> Edition</div>
  <div class="subtitle">
    <div class="subtitle-lead">The quiet geography of</div>
    <div class="subtitle-main">Tidal winds,<br>ferry routes and<br>harbour lanterns</div>
  </div>
  <div class="front-rule" style="top:680px"></div>
  <div class="front-rule is-second" style="top:703px"></div>
  <div class="front-author">Rupert Calloway</div>
</main>
</body>
</html>
```